fernvale junk clearing

A 6 flyer design.......
I have up loaded our company logo ....must use
A location map...........must use
and our business card with our contact information......please add all contact info
our ph. number must bold and prominent feature.....use use

A reliable Asbestos Removal & Demolition service that you can trust. All our services are offered at realistic prices and delivered on time. We operate 24 / 7 and provide free no-obligation quotes with good old fashion service.

We service the following towns and surrounding areas 7
days a week & 24 hours
Kempsey
Taree
South West Rocks
foster / Tuncurry
Coffs harbour
Nambucca Heads
Newcastle
Maitland
Singleton
Muswellbrook
Upper Hunter Valley
Central Coast
Tamworth
Armidale
this is an easy design as I have most of the theme and colours

```html
<!DOCTYPE html>
<html lang="en">
<head>
<meta charset="utf-8">
<title>Fernvale Junk Clearing – Flyer</title>
<link href="https://fonts.googleapis.com/css2?family=Open+Sans:wght@400;700;800&family=Roboto+Condensed:wght@700&display=swap" rel="stylesheet">
<style>
  :root{
    --green:#1fa12e;
    --green-mid:#178a26;
    --green-deep:#0f5e1c;
    --green-dark:#0b3b12;
    --ink:#1a3312;
    --text:#1b1b1b;
    --grey-band:#7d7d7d;
    --grey-panel:#d9d9d9;
    --white:#ffffff;
    --paper-bg:#ffffff;
  }
  *{box-sizing:border-box;margin:0;padding:0}
  html,body{width:1200px;height:1000px;overflow:hidden;background:var(--paper-bg)}
  body{position:relative;font-family:"Open Sans",Arial,sans-serif}
  .flyer{position:absolute;left:78px;top:138px;width:1048px;height:742px;background:var(--white);overflow:hidden}
  .stripes{position:absolute;left:0;top:0;width:1048px;height:742px}
  .brand-name{position:absolute;left:44px;top:40px;width:230px;font-weight:800;font-size:24px;line-height:1.1;color:var(--green-mid);text-transform:uppercase}
  .brand-mark{position:absolute;left:44px;top:102px;width:40px;height:40px;background:var(--green)}
  .tagline{position:absolute;left:297px;top:37px;width:300px;font-weight:700;font-size:19px;line-height:25px;color:var(--ink)}
  .phone{position:absolute;left:296px;top:118px;font-weight:800;font-size:40px;letter-spacing:.5px;color:var(--ink)}
  .service-photo{position:absolute;top:196px;height:180px;border:8px solid var(--green);border-radius:26px;transform:skewX(-22deg);overflow:hidden}
  .service-photo.asbestos{left:100px;width:300px;background:linear-gradient(120deg,#d9c64a 0%,#e8e6df 45%,#8d8a7c 100%)}
  .service-photo.demolition{left:398px;width:300px;background:linear-gradient(120deg,#6d5a47 0%,#c58a2a 50%,#4a3c30 100%)}
  .service-photo.rubbish{left:700px;width:300px;background:linear-gradient(120deg,#6e6258 0%,#b8aea0 50%,#3e3a38 100%)}
  .service-band{position:absolute;left:0;top:399px;width:1048px;height:48px;background:var(--grey-band)}
  .service-band span{position:absolute;top:7px;font-weight:700;font-size:29px;color:var(--white);letter-spacing:.3px}
  .accent-line{position:absolute;left:0;top:447px;width:1048px;height:15px;background:var(--green)}
  .info-panel{position:absolute;left:0;top:462px;width:1048px;height:280px;background:var(--grey-panel)}
  .intro{position:absolute;left:35px;top:480px;width:750px;font-size:18.5px;line-height:24px;color:var(--text)}
  .areas{position:absolute;left:35px;top:570px;width:740px;font-family:"Roboto Condensed",Arial,sans-serif;font-weight:700;font-size:17.5px;line-height:22.5px;color:var(--green-deep)}
  .coverage-map{position:absolute;left:700px;top:462px;width:348px;height:280px}
  .contact-bar{position:absolute;left:0;top:682px;width:760px;height:60px;background:var(--green);clip-path:polygon(0 0,100% 0,94% 100%,0 100%)}
  .contact-bar p{position:absolute;left:35px;top:17px;font-weight:700;font-size:17px;color:var(--white);white-space:nowrap}
  .contact-bar .sep{margin:0 16px}
</style>
</head>
<body>
<div class="flyer">
  <svg class="stripes" viewBox="0 0 1048 742" aria-hidden="true">
    <polygon points="640,0 1030,0 880,399 470,399" fill="#1fa12e"/>
    <polygon points="690,0 760,0 620,399 550,399" fill="#178a26"/>
    <polygon points="760,0 860,0 710,399 610,399" fill="#0b3b12"/>
    <polygon points="860,0 900,0 760,399 720,399" fill="#0f5e1c"/>
    <polygon points="930,0 970,0 820,399 780,399" fill="#178a26"/>
  </svg>

  <div class="brand-name">Fernvale<br>Junk Clearing</div>
  <div class="brand-mark"></div>

  <p class="tagline">Local Company Servicing the locals! Call us today for a free quote</p>
  <p class="phone">0491570156</p>

  <div class="service-photo asbestos" role="img" aria-label="Worker in protective suit and respirator behind an asbestos hazard fence"></div>
  <div class="service-photo demolition" role="img" aria-label="Excavator demolishing a building amid rubble"></div>
  <div class="service-photo rubbish" role="img" aria-label="Pile of discarded electronics and household junk"></div>

  <div class="service-band">
    <span style="left:82px">ASBESTOS REMOVAL</span>
    <span style="left:452px">DEMOLITION</span>
    <span style="left:707px">RUBBISH REMOVAL</span>
  </div>
  <div class="accent-line"></div>

  <div class="info-panel"></div>
  <div class="coverage-map" role="img" aria-label="Map of the NSW mid coast and Hunter region with a green circle marking the service area" style="background:linear-gradient(90deg,#f4e9a0 0%,#f4e9a0 70%,#a9d3ea 80%,#a9d3ea 100%);clip-path:polygon(30% 0,100% 0,100% 100%,0 100%)"></div>

  <p class="intro">A reliable <strong>Asbestos Removal &amp; Demolition</strong> service that you can trust. All our services are offered at realistic prices and delivered on time. We operate 24 / 7 and provide free no-obligation quotes with good old fashion service.</p>
  <p class="areas">We service the following towns and surrounding areas 7 days a week &amp; 24 hours – Kempsey, Taree, South West Rocks, Foster / Tuncurry, Coffs Harbour, Nambucca Heads, Newcastle, Maitland, Singleton, Muswellbrook, Upper Hunter Valley, Central Coast, Tamworth and Armidale.</p>

  <div class="contact-bar">
    <p>hello@fernvalejunkclearing.com<span class="sep">/</span>www.fernvalejunkclearing.com</p>
  </div>
</div>
</body>
</html>
```